Flyer-Design für Tauchsafaris, Vollcharter und Mini Safaris am roten Meer
Zielgruppe
Koralo Diving Safari
Wir sind ein Unternehmen, welches im Roten Meer Tauchsafaris, Vollcharter und Mini Safaris durchführt. Unsere Zielgruppe sind Taucher. Wir benötigen einen ansprechenden Flyer, welchen wir an Messen und auf den Booten an pozenziellen Kunden weitergeben können.
Aufgabenstellung
Der Flyer wird in Englisch sein. Anbei ist eine Worddatei angehängt mit den Textvorschlägen, die wir mal so besprochen haben. Das Layout muss nicht beachtet werden, es hat uns nur zur Übersich gedient. Unser jetztiger Flyer ist ein Falzflyer über 6 Seiten. Aber vielleicht macht auch ein anderers Mass sinn.
Wir haben sehr viele Bilder zur Verfügung, wenn etwas spezielles gebraucht wird.

```html
<!DOCTYPE html>
<html lang="en">
<head>
<meta charset="utf-8">
<title>Koralo Diving Safari – Mini Safari Flyer</title>
<link rel="stylesheet" href="https://fonts.googleapis.com/css2?family=Open+Sans:wght@400;600&display=swap">
<style>
  :root {
    --ink-blue: #2467a3;
    --paper: #ffffff;
    --paper-tint: #e9f1f8;
    --logo-ink: #1d2a3a;
    --sky-top: #3f8fd6;
    --sky-bottom: #a9cdef;
    --sea-top: #2a6fae;
    --sea-bottom: #1b4f86;
  }
  * { box-sizing: border-box; margin: 0; padding: 0; }
  html, body { width: 1200px; height: 2523px; overflow: hidden; background: var(--paper); }
  .flyer-panel {
    position: relative;
    width: 1200px;
    height: 2523px;
    overflow: hidden;
    font-family: "Open Sans", Arial, sans-serif;
    background: linear-gradient(to bottom, var(--paper) 40%, var(--paper-tint) 100%);
  }
  .boat-photo {
    position: absolute;
    left: 0; top: 0;
    width: 1200px; height: 905px;
    background:
      linear-gradient(to bottom, var(--sky-top) 0%, var(--sky-bottom) 66%, var(--sea-top) 66.5%, var(--sea-bottom) 100%);
  }
  .brand-tag {
    position: absolute;
    left: 0; top: 0;
    width: 390px; height: 177px;
    background: var(--paper);
    display: flex;
    align-items: center;
    gap: 20px;
    padding: 0 22px;
  }
  .brand-mark {
    width: 84px; height: 84px;
    border-radius: 50%;
    background: var(--logo-ink);
    flex: none;
  }
  .brand-text { color: var(--logo-ink); font-weight: 400; }
  .brand-name { font-size: 27px; line-height: 1.15; text-transform: uppercase; }
  .brand-sub { font-size: 15px; line-height: 1.5; text-transform: uppercase; letter-spacing: 1px; }
  .content {
    position: absolute;
    left: 106px; top: 990px;
    width: 1080px;
    color: var(--ink-blue);
    white-space: nowrap;
  }
  .title {
    font-size: 62px;
    font-weight: 400;
    line-height: 75px;
    margin-bottom: 20px;
  }
  .copy {
    font-size: 45px;
    line-height: 75px;
    font-weight: 400;
  }
  .copy + .copy { margin-top: 75px; }
</style>
</head>
<body>
<main class="flyer-panel">
  <div class="boat-photo" role="img" aria-label="Photo of the safari boat Marlena cruising on calm blue sea under a clear sky"></div>

  <div class="brand-tag">
    <span class="brand-mark"></span>
    <div class="brand-text">
      <div class="brand-name">Koralo Diving Safari</div>
      <div class="brand-sub">Red Sea, Egypt</div>
    </div>
  </div>

  <section class="content">
    <h1 class="title">Mini Safari</h1>
    <p class="copy">
      Would you like to try what it's like to be on a boat<br>
      for longer? Do you get seasick easily and don't<br>
      know if a safari is suitable for you?<br>
      Don't you have that much time?<br>
      Then a mini safari is just right for you.<br>
      Our boat Marlena is equipped with everything<br>
      you need for a perfect safari.
    </p>
    <p class="copy">
      Built in: 2019<br>
      Length: 30m<br>
      Width: 8m
    </p>
    <p class="copy">
      Enjoy the beauty of Sataya in the southern part<br>
      of the Red Sea. The reef is home to a large<br>
      school of spinner dolphins. We offer respectful<br>
      swimming and snorkeling with dolphins, as well<br>
      as exciting reef dives.<br>
      An adventure for the whole family.
    </p>
  </section>
</main>
</body>
</html>
```